Clean business card with logo provided

I want a card that will stand out among the masses. I need the color and image to show professionalism and yet have a family appeal showing that I only deal with win/win scenarios. The back of the card will be used to take notes about the individual so I can use that in my database entry. I like modern design but need professionalism in it also. It needs to fit my "clean, safe, and affordable housing" motto. I need to be able to write on the file and update the card details for my employees.

Target Market(s)

Investors looking to make investment income through real estate

Industry/Entity Type

Real Estate

Contact Information for Business Card

Troy Vandemark
blank address, city, st, zip code
480-555-0147
troyvandemark@quillrentals.example
www.quillrentals.example

Font styles to use
Sans Serif

Requirements
Must have
• I would like the back of the card to have lines for info. example
• Met/Visited: Date:
• Interets:
Nice to have
• I want the cards color to match the logo background color. Font with details to be san serif and black. I want the card rectangular with square corners. Standard business card size. I would like to see cards designed with both images to see which i prefer more.

```html
<!DOCTYPE html>
<html lang="en">
<head>
<meta charset="utf-8">
<title>Quill Rentals LLC – Business Card</title>
<link href="https://fonts.googleapis.com/css2?family=Open+Sans:wght@400;600&family=Exo+2:wght@600&family=Arimo:wght@400&display=swap" rel="stylesheet">
<style>
  :root {
    --page: #ece9e4;
    --card-white: #f2f2f2;
    --ink: #111111;
    --black: #000000;
    --teal: #00a9c0;
    --white: #ffffff;
  }
  * { box-sizing: border-box; margin: 0; padding: 0; }
  html, body { width: 1200px; height: 909px; overflow: hidden; background: var(--page); }
  .canvas { position: relative; width: 1200px; height: 909px; }

  .card {
    position: absolute;
    width: 600px; height: 343px;
    overflow: hidden;
    box-shadow: 0 6px 18px rgba(0,0,0,.25);
  }

  /* Back (notes) side */
  .card-back { left: 80px; top: 80px; background: var(--card-white); }
  .card-back .brand {
    position: absolute; left: 50px; top: 46px;
    font-family: "Open Sans", sans-serif; font-weight: 600;
    font-size: 40px; letter-spacing: 4px; color: var(--ink);
  }
  .card-back .tagline {
    position: absolute; left: 52px; top: 104px;
    font-family: "Open Sans", sans-serif; font-size: 14px; color: var(--ink);
  }
  .card-back .note-lines { position: absolute; left: 0; top: 0; }
  .notes {
    position: absolute; left: 52px; top: 205px;
    font-family: "Arimo", sans-serif; font-size: 22px; line-height: 30px; color: var(--ink);
  }

  /* Front side */
  .card-front { left: 520px; top: 486px; background: var(--black); }
  .card-front .bands { position: absolute; left: 0; top: 0; }
  .card-front .brand {
    position: absolute; right: 50px; top: 48px; text-align: right;
    font-family: "Open Sans", sans-serif; font-weight: 600;
    font-size: 40px; letter-spacing: 4px; color: var(--teal);
  }
  .card-front .brand-dot {
    display: inline-block; width: 14px; height: 14px; border-radius: 50%;
    background: var(--white); margin-left: 10px; vertical-align: middle;
  }
  .card-front .tagline {
    position: absolute; right: 50px; top: 112px;
    font-family: "Open Sans", sans-serif; font-size: 14px; color: var(--teal);
  }
  .holder-name {
    position: absolute; left: 24px; top: 262px;
    font-family: "Exo 2", sans-serif; font-weight: 600; font-size: 28px; color: var(--ink);
  }
  .divider { position: absolute; left: 258px; top: 244px; width: 2px; height: 88px; background: var(--ink); }
  .contact {
    position: absolute; left: 272px; top: 244px; list-style: none;
    font-family: "Arimo", sans-serif; font-size: 15px; line-height: 22px; color: var(--ink);
  }
  .contact li { display: flex; align-items: center; gap: 8px; }
  .contact svg { width: 13px; height: 13px; flex: none; }
</style>
</head>
<body>
<main class="canvas">

  <section class="card card-back" aria-label="Card back with note lines">
    <div class="brand">QUILL RENTALS LLC</div>
    <div class="tagline">Providing clean, safe, and affordable housing</div>
    <svg class="note-lines" width="600" height="343" viewBox="0 0 600 343" aria-hidden="true">
      <g stroke="var(--ink)" stroke-width="1.2" fill="var(--ink)">
        <line x1="255" y1="222" x2="560" y2="222"/><path d="M560 217 L570 222 L560 227 Z"/>
        <line x1="210" y1="252" x2="560" y2="252"/><path d="M560 247 L570 252 L560 257 Z"/>
        <line x1="190" y1="282" x2="560" y2="282"/><path d="M560 277 L570 282 L560 287 Z"/>
      </g>
    </svg>
    <div class="notes">
      <p>Met/Visited: Date:</p>
      <p>Interets:</p>
      <p>Problems:</p>
    </div>
  </section>

  <section class="card card-front" aria-label="Card front">
    <svg class="bands" width="600" height="343" viewBox="0 0 600 343" aria-hidden="true">
      <polygon points="0,190 0,343 600,343 600,200 560,222 100,222" fill="var(--teal)"/>
      <polygon points="50,188 100,212 560,212 585,202 565,222 100,222 48,196" fill="var(--black)"/>
      <polygon points="55,182 102,204 558,204 590,194 562,212 100,212 50,188" fill="var(--white)"/>
    </svg>
    <div class="brand">QUILL RENTALS LLC<span class="brand-dot"></span></div>
    <div class="tagline">Providing clean, safe, and affordable housing</div>

    <div class="holder-name">Troy Vandemark</div>
    <div class="divider"></div>
    <ul class="contact">
      <li><svg viewBox="0 0 16 16"><path d="M4 1l3 3-2 2c1 2 3 4 5 5l2-2 3 3-2 3C7 15 1 9 1 3z" fill="var(--ink)"/></svg>480-555-0147</li>
      <li><svg viewBox="0 0 16 16"><circle cx="8" cy="8" r="6.5" fill="none" stroke="var(--ink)" stroke-width="1.6"/><path d="M1.5 8h13M8 1.5c3 3.5 3 9.5 0 13M8 1.5c-3 3.5-3 9.5 0 13" fill="none" stroke="var(--ink)" stroke-width="1.2"/></svg>www.quillrentals.example</li>
      <li><svg viewBox="0 0 16 16"><rect x="1" y="3" width="14" height="10" fill="none" stroke="var(--ink)" stroke-width="1.6"/><path d="M1 3l7 6 7-6" fill="none" stroke="var(--ink)" stroke-width="1.4"/></svg>troyvandemark@quillrentals.example</li>
      <li><svg viewBox="0 0 16 16"><path d="M8 15s5-5.5 5-9A5 5 0 0 0 3 6c0 3.5 5 9 5 9z" fill="var(--ink)"/><circle cx="8" cy="6" r="1.8" fill="var(--teal)"/></svg>742 Elm Row, Cedar Heights, IL 60499</li>
    </ul>
  </section>

</main>
</body>
</html>
```